Business Card for new Architectural Firm

I intend to practice in a rural mountain community in upstate NY, focusing on residential and light commercial projects, including second home / vacation properties. I wish to convey a feeling of rural outdoorsy modernity.

Color is important - bold and urbane. Secondary or tertiary colors preferred.

Font is important, idiosyncratic is ok

Optionally, I may choose to use the name Brackenfold Studio. If used as part of your design, all of the Must Haves are still required.

Images uploaded are logos I like

Industry/Entity Type

Residential

Contact Information for Business Card

Caldwell Prusinski
Architect (This word should stand alone or be associated with my name - not license number)
NY License No. 582163
caldwell@designcpx.com
607 394 2858

Font styles to use
Sans Serif
Decorative

Requirements
Must have
• Whatever files I need to best utilize your design
• PDF
• JPG
• EPS
• Vectorwhatsit
Nice to have
• Logo or element that can be incorporated into other print material.
• Could be a font based card
Should not have
• no clip art
• No templates
• no floor plans
• no building photographs

```html
<!DOCTYPE html>
<html lang="en">
<head>
<meta charset="utf-8">
<title>Caldwell Prusinski Architect — Business Card</title>
<link rel="stylesheet" href="https://fonts.googleapis.com/css2?family=Montserrat:wght@300;400&display=swap">
<style>
  :root {
    --backdrop: #e6e6e4;
    --card-light: #f7f7f5;
    --card-dark: #363636;
    --green: #7dbb3a;
    --ink: #4a4a4a;
    --ink-soft: #8a8a8a;
    --paper-text: #dcdcdc;
    --paper-soft: #b5b5b5;
  }
  * { box-sizing: border-box; margin: 0; padding: 0; }
  html, body {
    width: 1200px;
    height: 1000px;
    overflow: hidden;
    background: var(--backdrop);
    font-family: "Montserrat", sans-serif;
  }
  .sheet {
    width: 1200px;
    height: 1000px;
    display: flex;
    flex-direction: column;
    align-items: center;
    justify-content: center;
    gap: 60px;
  }
  .card {
    position: relative;
    width: 700px;
    height: 400px;
    box-shadow: 0 6px 18px rgba(0,0,0,0.12);
  }
  .card--light { background: var(--card-light); color: var(--ink); }
  .card--dark  { background: var(--card-dark); color: var(--paper-text); }

  .lockup {
    position: absolute;
    top: 118px;
    right: 95px;
    display: flex;
    align-items: center;
    gap: 18px;
  }
  .lockup__text { text-align: right; }
  .lockup__name {
    font-size: 36px;
    font-weight: 400;
    line-height: 1.1;
    color: var(--green);
    letter-spacing: -0.3px;
  }
  .lockup__role {
    margin-top: 8px;
    font-size: 15px;
    font-weight: 300;
    letter-spacing: 11px;
    margin-right: -11px;
    color: var(--ink-soft);
  }
  .card--dark .lockup__role { color: var(--paper-soft); }
  .lockup__square {
    width: 92px;
    height: 92px;
    background: var(--green);
  }

  .contact {
    position: absolute;
    left: 70px;
    right: 60px;
    top: 268px;
    display: flex;
    align-items: center;
    gap: 10px;
    font-size: 15px;
    font-weight: 400;
    white-space: nowrap;
  }
  .contact__dot {
    width: 7px;
    height: 7px;
    background: var(--green);
    flex: none;
  }
</style>
</head>
<body>
<main class="sheet">
  <section class="card card--light" aria-label="Business card, light side">
    <div class="lockup">
      <div class="lockup__text">
        <div class="lockup__name">Caldwell Prusinski</div>
        <div class="lockup__role">ARCHITECT</div>
      </div>
      <div class="lockup__square"></div>
    </div>
    <div class="contact">
      <span>607 - 394 - 2858</span><span class="contact__dot"></span>
      <span>caldwell@designcpx.com</span><span class="contact__dot"></span>
      <span>License No. 582163</span><span class="contact__dot"></span>
    </div>
  </section>

  <section class="card card--dark" aria-label="Business card, dark side">
    <div class="lockup">
      <div class="lockup__text">
        <div class="lockup__name">Caldwell Prusinski</div>
        <div class="lockup__role">ARCHITECT</div>
      </div>
      <div class="lockup__square"></div>
    </div>
    <div class="contact">
      <span>607 - 394 - 2858</span><span class="contact__dot"></span>
      <span>caldwell@designcpx.com</span><span class="contact__dot"></span>
      <span>License No. 582163</span><span class="contact__dot"></span>
    </div>
  </section>
</main>
</body>
</html>
```